Harborline Cover Stationary Design

We require stationary design for a new Life Insurance Business, Harborline Cover based in Melbourne Australia.
The logo for this business was successfully developed using Pixel Forum (refer attached) and all stationary will incorporate this logo design.
The layout of the stationary needs to be clear, modern and of a premium quality.
The colours to be incorporated are to be the same as those in the logo, as well as black.
Stationary required:
1) Business Card
2) Letter Head
3) With Compliments Slip
4) Envelope (both A4 and DL size)
Updates
Thanks to everyone who has submitted a design.
Hi all,
Industry/Entity Type
Business
Requirements
Must have
- For the Business Card - on front:
Company Logo: refer attached
Dorian Velk
CFP, BBUS (Acc), CA
Director
417 Marlow Parade, Kestwick, VIC 3472
T: 03 9647 2250
F: 03 9682 4037
M: 0400 917 356
email: dvelk@harborlinecover.example.au
Harborline Cover Pty Ltd trading as Harborline Cover is an Authorised Representative of QRT Wealth Advisory Pty Limited (this should be at the bottom of the business card and in very small font)
Background colour on card should be white.
For the Business Card -on back:
Company Logo. The Symbol within the logo could be bigger than the text.
www.harborlinecover.example.au
Background for the back of the card could be in either Black or white.
For the Letterhead & With Compliments Slip:
T: 03 9647 2250
F: 03 9682 4037
M: 0400 917 356
E: dvelk@harborlinecover.example.au
W: www.harborlinecover.example.au
Harborline Cover Pty Ltd trading as Harborline Cover is an Authorised Representative of QRT Wealth Advisory Pty Limited ABN 46 173 509 862 AFSL No. 518904 (this should be at the bottom/footer and be in a very small font)
Envelopes:
Other Must Haves:
Choices of Font Type and Colour should be relatively consistent across each item of stationary.
There should also be consistency in the font size for the Letterhead and With Compliments Slip.

```html
<!DOCTYPE html>
<html lang="en">
<head>
<meta charset="utf-8">
<title>Harborline Cover Letterhead</title>
<link rel="stylesheet" href="https://fonts.googleapis.com/css2?family=Tinos:wght@400&display=swap">
<style>
  :root {
    --backdrop: #e9eaea;
    --paper: #fefefe;
    --band-grey: #9c9d9c;
    --brand-green: #a6c41e;
    --brand-grey: #9a9b9a;
    --ink: #3a3a3a;
    --watermark: #f1f1f1;
    --text-font: "Tinos", "Times New Roman", serif;
  }
  * { margin: 0; padding: 0; box-sizing: border-box; }
  html, body {
    width: 1200px;
    height: 900px;
    overflow: hidden;
    background: var(--backdrop);
  }
  .letterhead {
    position: absolute;
    left: 74px;
    top: 25px;
    width: 1052px;
    height: 850px;
    background: var(--paper);
    overflow: hidden;
  }
  .header-band {
    height: 106px;
    background: var(--band-grey);
    display: flex;
    align-items: center;
    justify-content: center;
  }
  .header-band__name {
    font-family: var(--text-font);
    font-size: 22px;
    font-weight: 400;
    letter-spacing: 2px;
    color: var(--paper);
  }
  .brand {
    position: absolute;
    left: 53px;
    top: 158px;
    display: flex;
    align-items: center;
    gap: 12px;
  }
  .brand__dot {
    width: 40px;
    height: 40px;
    border-radius: 50%;
    background: var(--brand-green);
  }
  .brand__name {
    font-family: var(--text-font);
    font-size: 32px;
    font-weight: 400;
    letter-spacing: 1.5px;
    color: var(--brand-green);
  }
  .sender-address {
    position: absolute;
    left: 122px;
    top: 231px;
    font-family: var(--text-font);
    font-size: 13px;
    color: var(--ink);
    letter-spacing: 0.2px;
  }
  .corner-watermark {
    position: absolute;
    right: 0;
    bottom: 0;
    width: 290px;
    height: 330px;
  }
</style>
</head>
<body>
  <main class="letterhead">
    <header class="header-band">
      <span class="header-band__name">Harborline Cover</span>
    </header>

    <div class="brand">
      <span class="brand__dot"></span>
      <span class="brand__name">Harborline Cover</span>
    </div>

    <p class="sender-address">417 Marlow Parade, Kestwick, VIC 3472</p>

    <svg class="corner-watermark" viewBox="0 0 290 330" aria-hidden="true">
      <circle cx="290" cy="330" r="300" fill="var(--watermark)"/>
    </svg>
  </main>
</body>
</html>
```